Label Design for an exciting food startup introducing millets to North America!

We need a label for Millet grains (and millet flour after design is finalized for the grains because it will be very similar except for the description) Looking for a clean, minimalistic design. Modern feel. We are a social enterprise introducing millet based products to North American Market and we cater to the customers who are health conscious, eat plant-based foods, may have gluten allergies and are looking for a healthy substitutes for carbohydrate-rich foods.Millets are a great alternative for rice/barley/couscous/quinoa. Very nutritious grain!Our big audacious goal is to make Millets the new Quinoa in the next 3 years!!! More information about the company can be found on the website koshafoods.comMore information in the brief attached.

Target Market(s)

Women (75%) and men (25%) aged 21-60 who are health conscious, want to eat vegan/plant based foods, willing to experiment with new foods. They care about the environment and doing good while choosing products that are good for them and the planet.

Industry/Entity Type

Food Production

Colors

Designer to choose colors to be used in the design.

Requirements
Must have
• Covered in the project brief attached
Nice to have
Should not have

```html
<!DOCTYPE html>
<html lang="en">
<head>
<meta charset="utf-8">
<title>Ravelun Meals – Millet Grain Pouch</title>
<link href="https://fonts.googleapis.com/css2?family=Delius&family=Kaushan+Script&family=Zilla+Slab:wght@400&family=Oswald:wght@500&family=Roboto:wght@400;700&display=swap" rel="stylesheet">
<style>
  :root{
    --backdrop:#f8ede2;
    --pouch:#f7f7f5;
    --ink:#1c1c1c;
    --ink-soft:#444;
    --leaf-green:#7ab648;
    --title-green:#7cbf4a;
    --grain-red:#a3232b;
    --brand-orange:#e0672b;
    --recipe-orange:#ee8a4a;
    --millet-gold:#e6c444;
    --millet-deep:#cfa526;
    --maple-red:#c8202a;
  }
  *{box-sizing:border-box;margin:0;padding:0}
  html,body{width:1200px;height:900px;overflow:hidden;background:var(--backdrop)}
  .canvas{position:relative;width:1200px;height:900px;background:var(--backdrop)}

  .pouch{position:absolute;top:140px;width:438px;height:640px;background:var(--pouch);overflow:hidden;box-shadow:0 10px 30px rgba(120,90,60,.12)}
  .pouch--front{left:162px}
  .pouch--back{left:666px}
  .pouch__band{position:absolute;left:0;right:0;bottom:0;height:84px;background:var(--leaf-green)}
  .abs{position:absolute}

  /* front */
  .claims{font-size:14px;line-height:19px;color:var(--ink)}
  .claims--health{left:18px;top:100px;font-family:"Kaushan Script",cursive}
  .claims--nutrition{left:294px;top:100px;font-family:"Delius",sans-serif;font-size:13px;letter-spacing:.5px}
  .brand-name{font-family:"Zilla Slab",serif;color:var(--brand-orange);white-space:nowrap}
  .brand-name--front{left:0;right:0;top:166px;text-align:center;font-size:27px}
  .brand-dot{display:block;width:34px;height:34px;border-radius:50%;background:var(--brand-orange);margin:0 auto 10px}
  .product-title{left:110px;top:230px;font-family:"Delius",sans-serif;font-size:108px;line-height:1;color:var(--title-green);letter-spacing:-2px}
  .product-subtitle{left:132px;top:320px;font-family:"Kaushan Script",cursive;font-size:54px;color:var(--grain-red);transform:rotate(-6deg)}
  .attributes{left:48px;top:438px;font-family:"Delius",sans-serif;font-size:16px;color:var(--ink-soft);list-style:none}
  .attributes li{display:flex;align-items:center;gap:14px;height:32px}
  .attributes svg{width:16px;height:16px}
  .net-weight{left:318px;top:490px;font-family:"Kaushan Script",cursive;font-size:16px;color:var(--grain-red);transform:rotate(-5deg)}
  .stalk-illustration{left:182px;top:336px;width:216px;height:220px;background:radial-gradient(ellipse at 60% 50%,rgba(150,150,150,.18),rgba(150,150,150,0) 70%)}
  .millet-pile--front{left:74px;top:520px;width:330px;height:120px;border-radius:50% 50% 0 0/60% 60% 0 0;background:radial-gradient(ellipse at 50% 40%,var(--millet-gold),var(--millet-deep))}

  /* back */
  .millet-pile--back{left:170px;top:0;width:268px;height:124px;border-radius:0 0 0 70%;background:radial-gradient(ellipse at 70% 20%,var(--millet-gold),var(--millet-deep))}
  .soup-bowl{left:314px;top:118px;width:120px;height:148px;border-radius:50%;background:radial-gradient(ellipse at 50% 45%,#e18b45 0,#c0692e 55%,#a66a3d 70%)}
  .grain-sketch{left:330px;top:250px;width:100px;height:80px;background:radial-gradient(ellipse,rgba(150,150,150,.18),rgba(150,150,150,0) 70%)}
  .brand-name--back{left:72px;top:146px;font-size:19px;display:flex;align-items:center;gap:8px}
  .brand-name--back .brand-dot{width:24px;height:24px;margin:0}

  .nutrition{left:27px;top:234px;width:134px;border:1px solid var(--ink);padding:3px 4px;font-family:"Roboto",sans-serif;font-size:6px;color:var(--ink);line-height:1.3}
  .nutrition__title{font-size:10px;font-weight:700;line-height:1.1}
  .nutrition__serving{border-bottom:3px solid var(--ink);padding-bottom:2px}
  .nutrition__row{display:flex;justify-content:space-between;border-bottom:.5px solid var(--ink);padding:1px 0}
  .nutrition__row--bold{font-weight:700;font-size:7px}
  .nutrition__row--heavy{border-bottom:2px solid var(--ink)}
  .nutrition__row span:last-child{display:flex;gap:14px}
  .nutrition__row .indent{padding-left:6px}
  .nutrition__note{font-size:5px;padding-top:2px}

  .recipes__title{left:214px;top:240px;font-family:"Delius",sans-serif;font-size:15px;line-height:18px;color:var(--recipe-orange);letter-spacing:.6px}
  .recipes__text{left:214px;top:286px;width:200px;font-family:"Delius",sans-serif;font-size:7.4px;line-height:12px;color:var(--ink-soft)}
  .story{left:212px;top:430px;display:flex;gap:14px;align-items:flex-start}
  .story__label{font-family:"Kaushan Script",cursive;font-size:13px;color:var(--ink)}
  .story__text{font-family:"Delius",sans-serif;font-size:9px;line-height:13px;color:var(--ink-soft);width:130px}
  .fine-print{left:214px;font-family:"Delius",sans-serif;font-size:6px;line-height:8px;color:#666;width:200px}
  .fine-print--ingredients{top:474px}
  .fine-print--maker{top:500px}
  .fine-print strong{font-weight:400;font-size:8px;color:var(--ink-soft);display:block}
  .recycle{left:154px;top:534px;font-family:"Oswald",sans-serif;font-size:8px;color:var(--ink-soft);text-align:center}
  .recycle svg{width:24px;height:24px;display:block;margin:0 auto 2px}
  .website{left:22px;top:582px;font-family:"Oswald",sans-serif;font-size:10px;letter-spacing:.6px;color:#2e3d1e}
  .origin{right:22px;top:572px;display:flex;align-items:center;gap:8px;font-family:"Oswald",sans-serif;font-size:10px;line-height:11px;color:#263418}
  .origin__mark{width:24px;height:24px;background:var(--maple-red)}
</style>
</head>
<body>
<main class="canvas">

  <section class="pouch pouch--front">
    <div class="pouch__band"></div>
    <div class="abs stalk-illustration" role="img" aria-label="Line drawing of a millet stalk with seed heads"></div>
    <div class="abs millet-pile--front" role="img" aria-label="Photograph of a heap of golden millet grains"></div>

    <ul class="abs claims claims--health" style="list-style:none">
      <li>• Low Glycemic Index</li>
      <li>• Diabetic friendly</li>
    </ul>
    <ul class="abs claims claims--nutrition" style="list-style:none">
      <li>• Source of Protein,</li>
      <li>• Fibre and minerals</li>
    </ul>

    <div class="abs brand-name brand-name--front"><span class="brand-dot"></span>Ravelun Meals</div>

    <h1 class="abs product-title">Millet</h1>
    <div class="abs product-subtitle">Grain</div>

    <ul class="abs attributes">
      <li><svg viewBox="0 0 16 16"><circle cx="8" cy="8" r="6" fill="none" stroke="#e0a030" stroke-width="1.6"/></svg>Raw</li>
      <li><svg viewBox="0 0 16 16"><path d="M8 15V7M8 7C6 3 3 3 2 3M8 7c2-4 5-5 6-5" fill="none" stroke="#7ab648" stroke-width="1.6" stroke-linecap="round"/></svg>Vegan</li>
      <li><svg viewBox="0 0 16 16"><circle cx="8" cy="8" r="6.5" fill="none" stroke="#c8202a" stroke-width="1.6"/><path d="M3.5 3.5l9 9" stroke="#c8202a" stroke-width="1.6"/></svg>Gluten-Free</li>
    </ul>

    <div class="abs net-weight">450g (1lb)</div>
  </section>

  <section class="pouch pouch--back">
    <div class="pouch__band"></div>
    <div class="abs millet-pile--back" role="img" aria-label="Photograph of scattered golden millet grains"></div>
    <div class="abs soup-bowl" role="img" aria-label="Photograph of a wooden bowl of millet vegetable soup"></div>
    <div class="abs grain-sketch" role="img" aria-label="Line drawing of millet seed heads"></div>

    <div class="abs brand-name brand-name--back"><span class="brand-dot"></span>Ravelun Meals</div>

    <div class="abs nutrition">
      <div class="nutrition__title">Valeur nutritive</div>
      <div class="nutrition__serving">pour MD (MM)<br>(environ MD préparé)</div>
      <div class="nutrition__row"><span></span><span><span>Tel que vendu</span><span>Préparé</span></span></div>
      <div class="nutrition__row nutrition__row--bold nutrition__row--heavy"><span>Calories</span><span><span>####</span><span>####</span></span></div>
      <div class="nutrition__row"><span></span><span>% valeur quotidienne*</span></div>
      <div class="nutrition__row"><span><b>Lipides</b> ## g<br><span class="indent">saturés ## g<br>+ trans ## g</span></span><span><span>## %</span><span>## %</span></span></div>
      <div class="nutrition__row"><span><b>Glucides</b> ## g<br><span class="indent">Fibres ## g<br>Sucres ## g</span></span><span><span>## %</span><span>## %</span></span></div>
      <div class="nutrition__row"><span><b>Protéines</b> ## g</span><span></span></div>
      <div class="nutrition__row"><span><b>Cholestérol</b> ### mg</span><span></span></div>
      <div class="nutrition__row nutrition__row--heavy"><span><b>Sodium</b> #### mg</span><span><span>## %</span><span>## %</span></span></div>
      <div class="nutrition__row"><span>Potassium #### mg</span><span><span>## %</span><span>## %</span></span></div>
      <div class="nutrition__row"><span>Calcium #### mg</span><span><span>## %</span><span>## %</span></span></div>
      <div class="nutrition__row nutrition__row--heavy"><span>Fer ## mg</span><span><span>## %</span><span>## %</span></span></div>
      <div class="nutrition__note">* Teneur de l'aliment tel que vendu.<br>** Préparé avec de l'eau selon le mode d'emploi.<br>* 5 % ou moins c'est <b>peu</b>, 15 % ou plus c'est <b>beaucoup</b></div>
    </div>

    <h2 class="abs recipes__title">Simple &amp; Easy<br>Millet Recipes!</h2>
    <p class="abs recipes__text">Rinse one cup of millet and toast it in a dry pan until fragrant. Add two cups of water or broth and a pinch of salt. Bring to a boil, cover and simmer for fifteen minutes. Let it rest, then fluff with a fork. Serve warm as a side, toss into soups and salads, or stir into a hearty vegetable stew for a filling and wholesome meal any day of the week.</p>

    <div class="abs story">
      <span class="story__label">Our story</span>
      <span class="story__text">Produced through a partnership with farmers in India</span>
    </div>

    <p class="abs fine-print fine-print--ingredients">Ingredients: Whole grain millets<br>Origin: India</p>
    <p class="abs fine-print fine-print--maker"><strong>Manufactured By</strong>Ravelun Meals Inc., 120 Harvest Lane, Unit 4. Store in a cool dry place. Reseal after opening to keep your grains fresh for longer.</p>

    <div class="abs recycle">
      <svg viewBox="0 0 24 24"><path d="M12 3l4 6h-3v5h-2V9H8zM4 19l3-6 2 3 4-1-1 2-3 1 1 2zM20 19l-3-6-2 3 1 2h-3l-1 2h7z" fill="#4aa44a"/></svg>
      RECYCLE
    </div>

    <div class="abs website">WWW.RAVELUNMEALS.COM</div>
    <div class="abs origin"><span class="origin__mark" role="img" aria-label="Red maple leaf emblem"></span>PACKAGED<br>IN CANADA</div>
  </section>

</main>
</body>
</html>
```